the kobo bite

we have a product called the kobo bite that we are looking for a label for the packaging - it is a weight loss chocolate bar for men only
its a low sugar low calorie healthy snack
our website is www.thetorvablend.com.au for more info about our company.
looking for a label design thats manly but also for the everyday person to eat
Our company colurs are blue, yellow and white.
Looking for something a bit quirky that grabs peoples attention.

```html
<!DOCTYPE html>
<html lang="en">
<head>
<meta charset="utf-8">
<title>the kobo bite – chocolate bar label</title>
<link rel="stylesheet" href="https://fonts.googleapis.com/css2?family=Open+Sans:ital,wght@0,700;0,800;1,600;1,700&display=swap">
<style>
  :root {
    --paper: #ffffff;
    --choc-dark: #3b2412;
    --choc-light: #5c3719;
    --choc-text: #5a3518;
    --panel: #6e4524;
    --yellow: #ffcc00;
    --ink: #111111;
    --white: #ffffff;
  }
  html, body {
    margin: 0;
    width: 1200px;
    height: 385px;
    overflow: hidden;
    background: var(--paper);
  }
  .label {
    position: relative;
    width: 1200px;
    height: 385px;
    font-family: "Open Sans", Arial, sans-serif;
  }
  .wrapper-band {
    position: absolute;
    left: 20px;
    top: 18px;
    width: 1162px;
    height: 350px;
    background: linear-gradient(90deg, var(--choc-dark) 0%, var(--choc-light) 100%);
  }
  .brand-name {
    position: absolute;
    left: 108px;
    top: 70px;
    margin: 0;
    color: var(--yellow);
    font-weight: 800;
    line-height: 1;
  }
  .brand-name .brand-article {
    display: block;
    font-size: 84px;
    letter-spacing: -2px;
  }
  .brand-name .brand-product {
    display: block;
    margin-top: 14px;
    font-size: 138px;
    letter-spacing: -3px;
  }
  .tagline {
    position: absolute;
    left: 462px;
    top: 88px;
    width: 322px;
    height: 40px;
    box-sizing: border-box;
    border: 2px solid var(--ink);
    border-radius: 9px;
    background: var(--yellow);
    color: var(--ink);
    font-style: italic;
    font-weight: 700;
    font-size: 24px;
    line-height: 36px;
    text-align: center;
  }
  .flavour {
    position: absolute;
    left: 905px;
    top: 72px;
    width: 214px;
    height: 54px;
    box-sizing: border-box;
    border: 2px solid var(--choc-dark);
    border-radius: 50%;
    background: var(--yellow);
    color: var(--choc-text);
    font-weight: 700;
    font-size: 29px;
    line-height: 48px;
    text-align: center;
  }
  .benefits {
    position: absolute;
    left: 900px;
    top: 160px;
    width: 234px;
    height: 160px;
  }
  .benefits svg { position: absolute; inset: 0; }
  .benefits ul {
    position: absolute;
    left: 30px;
    top: 26px;
    margin: 0;
    padding: 0;
    list-style: none;
    color: var(--yellow);
    font-style: italic;
    font-weight: 600;
    font-size: 23px;
    line-height: 38px;
  }
  .benefits li:nth-child(2) { padding-left: 0; margin-left: -6px; }
  .benefits li:nth-child(3) { margin-left: -14px; }
  .net-weight {
    position: absolute;
    left: 1114px;
    top: 304px;
    color: var(--white);
    font-style: italic;
    font-weight: 700;
    font-size: 24px;
  }
</style>
</head>
<body>
<main class="label">
  <div class="wrapper-band"></div>

  <h1 class="brand-name">
    <span class="brand-article">the</span>
    <span class="brand-product">KOBO BITE</span>
  </h1>

  <div class="tagline">Health bar for men</div>
  <div class="flavour">Chocolate</div>

  <section class="benefits">
    <svg width="234" height="160" viewBox="0 0 234 160" aria-hidden="true">
      <rect x="6" y="2" width="226" height="156" rx="14" fill="var(--yellow)"/>
      <rect x="12" y="8" width="222" height="152" rx="12" fill="var(--panel)"/>
    </svg>
    <ul>
      <li>Low sugar</li>
      <li>Low calorie</li>
      <li>Healthy snack</li>
    </ul>
  </section>

  <div class="net-weight">50g</div>
</main>
</body>
</html>
```